Architectural Footbridge Poster / Board

We are a design company specializing in bridge design and engineering. We have developed a footbridge design intended for use in local parks within New Zealand. With the help of our friends here at Artwork Hive have created 3D render of our bridge that we need turned into striking posters that can be used to advertise the bridge to local councils, architects, and private developers.

We have attached a series of high resolution raw images that we would like used in our posters. Feel free to select and/or crop the images to fit with your poster style. We have also included all of the text that we need added (see below). We would like the posters to appear professional but artistic/fun. We have created a quick mock-up using MS Word to give you an idea of what we need. Please note we expect the designers to vastly improve or in many cases drastically change these quick mock-ups and we will be looking at composition, alignment/layout, and style. Once we have an entry that we feel provide a high quality visual poster we will guarantee the payment.
The competition will be based on producing 2 posters: page 1 and page 2 as per the attached poster content.

• Poster layout must be landscape.
• Raw "InDesign", or "MS Word" or other pre-approved raw file must be supplied to receive payment. Alternative file types can be pre-approved via the comments field.
• The posters must be high resolution PDF to size A0.
• The poster will also be printed at A3. Minimum font size when viewed in A3 should be size 8 and readable (size 9 is preferred). Images can go all the way to the outside of the page but A3 text margins must be set a minimum 0.4cm from top and bottom and 1cm left and right.
• Some examples of architecture board styles that we like have been put in a Pinterest folder here: https://boards.pinlatch.example/MorvenTallisEng/architecture-display-board/
• If you think your style would be better achieved by splitting each page into two this will be considered if it lends significant style advantages. We will try to provide early feedback on this if we see good examples.
• Along the way we will be providing detailed feedback to our designers as required.
• If you need more text or info for a particular poster style let us know. Requesting more text is fine but further 3d renders are not possible. We will try to provide additional text as requested.
• We have included a company logo that was created very quickly by our team. Feel free to modify or improve this logo if it improves your poster design. Merit will be given to posters that significantly improve our logo. Our company creates vibrant and interesting footbridges.

Please be as creative as you can. If we like your style there is the potential for future work doing similar poster work for alternative bridge designs.

Let us know if you have any questions.

Target Market(s)

landscape architects, local councils

Industry/Entity Type

It Company

Requirements
Must have
• 1) Landscape orientation
• 2) Printable (and readable) at both A0 and A3
• 3) Raw InDesign, Photoshop, MS Word or other pre-approved raw file type.
Nice to have
• Posters should be image focussed with text being less prominent.

```html
<!DOCTYPE html>
<html lang="en">
<head>
<meta charset="utf-8">
<title>Pedestrian &amp; Cycle Friendly Footbridge Design Set</title>
<link href="https://fonts.googleapis.com/css2?family=Oswald:wght@500&family=Roboto+Condensed:wght@400;700&display=swap" rel="stylesheet">
<style>
:root{
  --bg:#d9d9d9;
  --paper:#f2f2f2;
  --ink:#1e1e1e;
  --heading-red:#8b1a10;
  --deep-red:#5c0b08;
  --brand-red:#b8361a;
  --orange:#e0801f;
  --teal:#0e4447;
  --teal-text:#0d4a4a;
  --slate:#2d2d2d;
  --grey-strip:#cfcfcf;
  --rule:#8aa6a6;
}
*{margin:0;padding:0;box-sizing:border-box}
html,body{width:1200px;height:917px;overflow:hidden}
body{background:var(--bg);font-family:"Roboto Condensed",Arial,sans-serif;color:var(--ink)}
.poster{position:absolute;left:30px;top:56px;width:1139px;height:805px;background:linear-gradient(90deg,#ececec,#f6f6f6 40%,#e6e6e6);overflow:hidden}
.abs{position:absolute}
.header-band{left:0;top:0;width:1139px;height:78px}
.logo{left:13px;top:8px;font-size:38px;font-weight:400;letter-spacing:.5px;color:var(--ink);line-height:48px}
.set-title{left:570px;top:12px;font-family:"Oswald",sans-serif;font-weight:500;font-size:26px;color:#fff;line-height:40px;white-space:nowrap}
.set-title .underlined{border-bottom:2px solid #fff;padding-bottom:1px}
.hero{left:440px;top:84px;width:699px;height:326px}
.hero-band{left:440px;top:330px;width:699px;height:80px}
.hero-questions{left:630px;top:340px;list-style:none;color:#fff;font-size:11px;line-height:19px}
.hero-questions li{position:relative;padding-left:12px}
.hero-questions li::before{content:"";position:absolute;left:0;top:8px;width:4px;height:4px;background:#fff}
.section-heading{font-weight:700;font-size:11.5px;color:var(--heading-red);white-space:nowrap;display:flex;align-items:center}
.section-heading::after{content:"";display:inline-block;width:120px;height:2px;background:var(--teal);margin-left:8px}
.intro{left:13px;top:88px;width:459px}
.intro p{font-size:10px;line-height:15.8px;text-align:justify;margin-top:8px}
.intro p+p{margin-top:9px}
.audience-label{left:0;top:334px;width:405px;height:20px}
.audience-label span{position:absolute;left:14px;top:2px;color:#fff;font-weight:700;font-size:12px;letter-spacing:.3px}
.audience{left:18px;top:366px;width:420px;display:grid;grid-template-columns:201px 200px;row-gap:4px;list-style:none}
.audience li{font-size:11px;font-weight:700;color:var(--teal-text);letter-spacing:.3px;position:relative;padding-left:12px}
.audience li::before{content:"";position:absolute;left:0;top:4px;width:5px;height:5px;background:var(--teal-text)}
.photo{display:block}
.why-panel{left:385px;top:418px;width:754px;height:162px;background:linear-gradient(90deg,#e8e8e8,#d6d6d6)}
.why-panel .section-heading{position:absolute;left:9px;top:9px}
.col{position:absolute;font-size:10px;line-height:17.2px;text-align:justify}
.divider{position:absolute;width:1px;background:var(--rule)}
.bar{position:absolute}
.next-panel{left:0;top:590px;width:757px;height:206px;background:linear-gradient(90deg,#f0f0f0,#e2e2e2)}
.next-panel .section-heading{position:absolute;left:13px;top:8px}
</style>
</head>
<body>
<div class="poster">

  <svg class="abs header-band" viewBox="0 0 1139 78" aria-hidden="true">
    <defs>
      <linearGradient id="redBand" x1="0" y1="0" x2="1" y2="0">
        <stop offset="0" stop-color="#c5441b"/>
        <stop offset=".35" stop-color="#8f1a0e"/>
        <stop offset="1" stop-color="#5a0a08"/>
      </linearGradient>
    </defs>
    <rect x="0" y="0" width="460" height="64" fill="#fff"/>
    <polygon points="0,64 458,64 469,78 0,78" fill="var(--grey-strip)"/>
    <polygon points="458,64 500,64 510,78 469,78" fill="#9a9a9a"/>
    <polygon points="426,0 478,0 510,56 458,56" fill="var(--slate)"/>
    <polygon points="474,0 534,0 570,78 510,78" fill="var(--orange)"/>
    <polygon points="526,0 1139,0 1139,78 562,78" fill="url(#redBand)"/>
    <polygon points="560,0 610,0 646,78 596,78" fill="#ffffff" opacity=".06"/>
    <polygon points="650,0 690,0 726,78 686,78" fill="#000000" opacity=".06"/>
  </svg>

  <div class="abs logo">KEELROW BRIDGEWORKS</div>
  <div class="abs set-title">PEDESTRIAN &amp; CYCLE FRIENDLY <span class="underlined">FOOTBRIDGE DESIGN SET</span></div>

  <svg class="abs" style="left:470px;top:240px;width:180px;height:170px" viewBox="0 0 180 170" aria-hidden="true">
    <polygon points="80,0 156,170 0,170" fill="#cfcfcf"/>
    <polygon points="110,40 170,170 60,170" fill="#bdbdbd"/>
  </svg>

  <svg class="abs hero" viewBox="0 0 699 326" role="img" aria-label="Render of the footbridge crossing a turquoise pond in an autumn park with willows and coloured trees">
    <defs>
      <linearGradient id="heroSky" x1="0" y1="0" x2="1" y2="1">
        <stop offset="0" stop-color="#c98a2a"/>
        <stop offset=".35" stop-color="#5e7a3a"/>
        <stop offset=".6" stop-color="#7ea35a"/>
        <stop offset=".8" stop-color="#3fb3b8"/>
        <stop offset="1" stop-color="#2b8f9a"/>
      </linearGradient>
    </defs>
    <polygon points="34,0 699,0 699,326 186,326" fill="#fff"/>
    <polygon points="44,0 699,0 699,326 196,326" fill="url(#heroSky)"/>
  </svg>
  <svg class="abs hero-band" viewBox="0 0 699 80" aria-hidden="true">
    <polygon points="149,0 699,0 699,80 186,80" fill="var(--teal)" opacity=".88"/>
  </svg>
  <ul class="abs hero-questions">
    <li>Are you a landscape architect, developer, or local council looking to create or improve a public space?</li>
    <li>Do areas of your design require pedestrian or cycle friendly bridges?</li>
    <li>Does your project budget make engaging bridge engineers difficult at this stage of your design process?</li>
  </ul>

  <div class="abs intro">
    <h2 class="section-heading">THE “KBW PEDESTRIAN BRIDGE”</h2>
    <p>This bridge set is a simple and cost effective bridge solution for use in parks and urban landscapes. It is designed to New Zealand standards by experienced and qualified bridge engineers and bridge architects. The aim of this bridge design is to establish a baseline pedestrian bridge design for New Zealand that can be easily implemented into most New Zealand design situations.</p>
    <p>The bridge design is a steel beam system supporting timber joist and decking. The bridge can carry pedestrians and cyclists and allows spans of up to 18m and usable widths up to 3m. Various balustrades designs are provided and the colour of the steelwork is fully customisable without further design inputs.</p>
    <p>This bridge set is intended to help designers who need a simple cost effective bridge for their overall masterplan but who do not want to commission a bridge engineer or bridge architect in the early stages. In many cases the design can be successfully modified using variations of colour and balustrade type to fit the specific context without further design inputs being required.</p>
  </div>

  <div class="abs audience-label">
    <svg width="405" height="20" viewBox="0 0 405 20" aria-hidden="true"><polygon points="0,0 405,0 397,20 0,20" fill="var(--teal)"/></svg>
    <span>The design is intended to help the following professionals:</span>
  </div>
  <ul class="abs audience">
    <li>LANDSCAPE ARCHITECTS</li>
    <li>DEVELOPERS</li>
    <li>COUNCILS &amp; LOCAL BOARDS</li>
    <li>DESIGN AND BUILD CONTRACTORS</li>
  </ul>

  <svg class="abs photo" style="left:8px;top:418px" width="368" height="162" viewBox="0 0 368 162" role="img" aria-label="Render of people walking across the timber deck of the footbridge under autumn trees">
    <defs>
      <linearGradient id="deckPhoto" x1="0" y1="0" x2="0" y2="1">
        <stop offset="0" stop-color="#7a5a2a"/>
        <stop offset=".45" stop-color="#4f6a3a"/>
        <stop offset=".7" stop-color="#3d8f95"/>
        <stop offset="1" stop-color="#cdb898"/>
      </linearGradient>
    </defs>
    <rect width="368" height="162" fill="url(#deckPhoto)"/>
  </svg>
  <div class="bar" style="left:0;top:580px;width:385px;height:8px;background:var(--teal)"></div>

  <div class="abs why-panel">
    <h2 class="section-heading">Why do we need a baseline pedestrian bridge design in NZ?</h2>
    <p class="col" style="left:9px;top:34px;width:351px">These designs are intended to be used for concept and feasibility stages of urban and landscape design projects. Landscape designers and councils often ask us if there are any basic bridge designs they can use to begin setting their overall masterplan and capital budgets. Until now the answer has always been “no”. As of 2017 none of the local councils of NZ or the National Roading Board have standard designs for pedestrian or cycle bridges that are readily available to designers.</p>
    <div class="divider" style="left:375px;top:38px;height:112px"></div>
    <p class="col" style="left:389px;top:34px;width:351px">In the early stages of a project; councils, developers, and landscape designers want simple and reliable bridge options that fit to, and help set, their overall budgets. Making this design set freely available to all professionals is aimed at encouraging and more easily enhancing public spaces in and around NZ. This set aims to enable landscape architects and urban designers to setup public space masterplans and overall capital budgets that their clients can readily understand and hopefully accept prior to engaging other professionals.</p>
  </div>
  <div class="bar" style="left:385px;top:580px;width:754px;height:8px;background:var(--orange)"></div>

  <div class="abs next-panel">
    <h2 class="section-heading">So you have set a masterplan and you have agreed a capital budget using this bridge design… what next?</h2>
    <p class="col" style="left:11px;top:32px;width:351px">The bridge beams, decking and balustrades of this design set are pre-designed ready for construction to New Zealand standards as outlined in the New Zealand Building Code (as of January 2017). This approach to the design is intended to save your project time and money. At building consent stage and in accordance with the New Zealand Building Code a Designer Producer Statement (PS1) for the bridge structure and PS1 for Geotechnical work will be required. Such services can be provided by your existing chartered professional engineering professionals (CPEng) once they have satisfied themselves that the design is compliant. Alternatively, you can contact us at Keelrow Bridgeworks Ltd to provide these services.</p>
    <div class="divider" style="left:376px;top:28px;height:170px"></div>
    <p class="col" style="left:391px;top:32px;width:351px">Prior to resource consenting a small geotechnical study will be necessary to confirm the ground conditions, geotechnical design parameters and provide bridge foundation recommendations. This is likely to consist of two borehole tests (one at each abutment location) followed by a small report summarising the ground conditions, geotechnical properties, and substructure recommendations. This study will then be used by your structural engineering design professional to design and detail a suitable abutment to support the bridge.</p>
  </div>

  <svg class="abs photo" style="left:762px;top:590px" width="369" height="204" viewBox="0 0 369 204" role="img" aria-label="Aerial render of the footbridge deck spanning clear blue water with a cyclist and scattered autumn leaves">
    <defs>
      <linearGradient id="aerialPhoto" x1="0" y1="0" x2="1" y2="1">
        <stop offset="0" stop-color="#3f5a3a"/>
        <stop offset=".4" stop-color="#8a7362"/>
        <stop offset=".7" stop-color="#6f5f55"/>
        <stop offset="1" stop-color="#2fa0d8"/>
      </linearGradient>
    </defs>
    <rect width="369" height="204" fill="url(#aerialPhoto)"/>
  </svg>

  <svg class="bar" style="left:0;top:796px" width="1139" height="9" viewBox="0 0 1139 9" aria-hidden="true">
    <polygon points="0,0 752,0 758,9 0,9" fill="var(--orange)"/>
    <polygon points="760,0 1139,0 1139,9 766,9" fill="var(--teal)"/>
  </svg>

</div>
</body>
</html>
```